Haulvento tri-fold brochure, letterhead, business cards, envelopes.

I need a professional looking flyer that will appeal to shipping managers, dispatchers, etc. who don't have a lot of time. I'm Certified Freight Broker (title is a registered trademark) arranging freight transportation at the lowest possible cost to the shipper. I contract with shippers and then find truckers in the area that will backhaul and thus give the shipper a discounted transportation rate. I let the shipper tell me the rate they want to pay and I negotiate with trucking companies to find that rate. I'll upload the topics I want to convey. Keep in mind that the brochure has to be eye catching enough on the first page to entice them to read on. I want to tie into my website design a bit if possible. It's a simple site so I don't know just how well that'll work. I do want the brochure, business cards, letterhead and envelopes to tie in with each other. I'd like my picture on the brochure somewhere.

Target Market(s)

Shipping managers, trucking dispatchers.

Industry/Entity Type

Truckline Operation

Contact Information for Business Card

Professional design that will set off the logo colors.

Font styles to use
Serif
Sans Serif

Colors

Designer to choose colors to be used in the design.

Requirements
Must have
• Mark Velinstrom, CERTIFIED FREIGHT BROKERīƒ’
• Phone: 866-417-3961
• Email: Mark@haulvento.example
• Website: www.haulvento.example
• Business logo with "TM" to indicate trademark registration has been files.
• Tag line "Fast Shipping Relief".
• My photo.
Nice to have
• Address: 3175 W. Brindle Avenue, #51872
• Denver, CO 80391

```html
<!DOCTYPE html>
<html lang="en">
<head>
<meta charset="utf-8">
<title>Haulvento Freight Logistics – Tri-fold Brochure</title>
<link rel="stylesheet" href="https://fonts.googleapis.com/css2?family=Open+Sans:wght@400;600;700;800&display=swap">
<style>
  :root{
    --red:#d71f26;
    --red-dark:#9e1116;
    --charcoal:#2a2a2c;
    --paper:#ffffff;
    --page:#e4e4e4;
    --ink:#3a3a3a;
    --ink-soft:#6a6a6a;
  }
  *{box-sizing:border-box;margin:0;padding:0}
  html,body{width:1200px;height:2400px;overflow:hidden}
  body{background:var(--page);font-family:"Open Sans",Arial,sans-serif;color:var(--ink);position:relative}

  .spread{position:absolute;left:50px;width:1100px;height:850px;display:flex;box-shadow:0 12px 30px rgba(0,0,0,.18);background:var(--paper)}
  .spread--outside{top:230px}
  .spread--inside{top:1320px}
  .panel{position:relative;width:366.67px;height:850px;overflow:hidden}
  .panel + .panel{border-left:1px solid rgba(0,0,0,.06)}

  .photo{position:absolute}
  .shape{position:absolute}

  .brand{display:flex;align-items:center;gap:9px;font-weight:800;font-size:16px;letter-spacing:.4px;text-transform:uppercase;white-space:nowrap}
  .brand__square{width:14px;height:14px;flex:none}

  /* outside: flap */
  .flap .photo--sunset{left:0;top:0;width:100%;height:230px;background:linear-gradient(170deg,#f4b56a 0%,#c98a54 35%,#6f6f83 70%,#3d4254 100%)}
  .flap .shape--swoosh{left:0;top:150px;width:100%;height:120px;background:var(--charcoal);clip-path:polygon(0 55%,100% 0,100% 20%,0 75%)}
  .flap .shape--white{left:0;top:190px;width:100%;height:120px;background:var(--paper);clip-path:polygon(0 40%,100% 0,100% 100%,0 100%)}
  .flap .copy{position:absolute;left:40px;right:36px;top:280px}
  .section-title{color:var(--red);font-weight:700;font-size:14px;letter-spacing:1px;text-transform:uppercase;margin-bottom:8px}
  .body-text{font-size:13px;line-height:1.6;color:var(--ink-soft)}
  .flap .body-text + .section-title{margin-top:22px}
  .flap .shape--footer{left:0;bottom:0;width:100%;height:190px;background:var(--charcoal);clip-path:polygon(0 25%,100% 0,100% 100%,0 100%)}
  .flap .quote{position:absolute;left:0;right:0;bottom:72px;text-align:center;color:#fff;font-size:22px;letter-spacing:2px;text-transform:uppercase}
  .flap .web{position:absolute;left:0;right:0;bottom:36px;text-align:center;color:#cfcfcf;font-size:13px;letter-spacing:2px}

  /* outside: back panel */
  .back{background:linear-gradient(180deg,var(--red) 0%,var(--red-dark) 100%)}
  .back .shape--top{left:0;top:0;width:100%;height:220px;background:var(--charcoal);clip-path:polygon(0 0,100% 0,100% 70%,0 100%)}
  .back .brand{position:absolute;top:72px;left:0;right:0;justify-content:center;color:#fff}
  .back .brand__square{background:var(--red)}
  .back .portrait{position:absolute;left:50%;top:270px;width:130px;height:130px;margin-left:-65px;border-radius:50%;border:5px solid #fff;background:radial-gradient(circle at 50% 40%,#c9c9cc 0%,#8a8a90 60%,#5a5a60 100%)}
  .back .name{position:absolute;top:430px;left:0;right:0;text-align:center;color:#fff;font-size:22px;font-weight:600}
  .back .title{position:absolute;top:462px;left:0;right:0;text-align:center;color:#fff;font-size:15px;letter-spacing:1px;text-transform:uppercase}
  .contact{position:absolute;top:520px;left:60px;right:30px;list-style:none;color:#fff;font-size:14px}
  .contact li{display:flex;align-items:center;gap:12px;margin-bottom:16px}
  .contact svg{flex:none}
  .back .shape--bottom{left:0;bottom:0;width:100%;height:170px;background:var(--charcoal);clip-path:polygon(0 0,100% 30%,100% 100%,0 100%)}

  /* outside: cover */
  .cover .shape--head{left:0;top:0;width:100%;height:250px;background:var(--paper)}
  .cover .brand{position:absolute;top:84px;left:0;right:0;justify-content:center;color:var(--red)}
  .cover .brand__square{background:var(--charcoal)}
  .cover .photo--truck{left:0;top:180px;width:100%;height:480px;background:linear-gradient(160deg,#b5a896 0%,#a55234 35%,#7a2e1e 55%,#55504a 80%,#c8b070 100%);clip-path:polygon(0 20%,100% 0,100% 100%,0 100%)}
  .cover .shape--dark{left:0;top:170px;width:100%;height:120px;background:var(--charcoal);clip-path:polygon(0 55%,100% 0,100% 28%,0 82%)}
  .cover .shape--band{left:0;bottom:0;width:100%;height:260px;background:linear-gradient(180deg,var(--red) 0%,var(--red-dark) 100%);clip-path:polygon(0 28%,100% 0,100% 100%,0 100%)}
  .cover .tagline{position:absolute;left:0;right:0;bottom:110px;text-align:center;color:#fff;font-size:30px;font-weight:700}
  .cover .web{position:absolute;left:0;right:0;bottom:70px;text-align:center;color:#f2c5c7;font-size:14px;letter-spacing:2px}

  /* inside: left */
  .benefits{padding:80px 38px 0}
  .benefits .shape--corner{left:0;top:0;width:100%;height:90px;background:var(--red);clip-path:polygon(0 0,55% 0,0 100%)}
  .headline{font-size:25px;font-weight:800;line-height:1.25;color:var(--charcoal);margin-bottom:14px}
  .headline em{font-style:normal;color:var(--red)}
  .rule{width:70px;height:3px;background:var(--red);margin-bottom:22px}
  .benefits .body-text{margin-bottom:16px;font-size:14px}
  .benefits .shape--swoosh{left:0;bottom:0;width:100%;height:150px;background:var(--red);clip-path:polygon(0 30%,100% 75%,100% 100%,0 100%)}
  .benefits .shape--grey{left:0;bottom:0;width:100%;height:150px;background:var(--charcoal);clip-path:polygon(0 60%,100% 100%,0 100%)}

  /* inside: middle */
  .network{background:linear-gradient(180deg,var(--red) 0%,var(--red-dark) 100%)}
  .network .photo--rig{left:0;top:0;width:100%;height:230px;background:linear-gradient(180deg,#cfe4ef 0%,#6b93b8 45%,#3d4e6a 75%,#8a7a6a 100%);clip-path:polygon(0 0,100% 0,100% 80%,0 100%)}
  .network .copy{position:absolute;left:36px;right:36px;top:260px;color:#fff}
  .network .lead{font-size:16px;font-weight:700;line-height:1.45;margin-bottom:18px}
  .network .rule{background:#fff}
  .network p{font-size:14px;line-height:1.55;margin-bottom:16px}
  .network .photo--yard{left:0;bottom:0;width:100%;height:200px;background:linear-gradient(180deg,#9b9b9b 0%,#6d6d6d 50%,#3f3f3f 100%);clip-path:polygon(0 22%,100% 0,100% 100%,0 100%)}

  /* inside: right */
  .service .photo--road{left:0;top:0;width:100%;height:240px;background:linear-gradient(170deg,#f3e6c8 0%,#d8b27a 40%,#9a8a7a 75%,#6e6a66 100%);clip-path:polygon(0 0,100% 0,100% 100%,0 70%)}
  .service .shape--wedge{left:0;top:150px;width:60%;height:120px;background:var(--red);clip-path:polygon(0 0,100% 75%,0 100%)}
  .service .copy{position:absolute;left:38px;right:34px;top:300px}
  .service .body-text{margin-bottom:24px}
  .service .shape--foot{left:0;bottom:0;width:100%;height:120px;background:var(--red);clip-path:polygon(0 80%,100% 40%,100% 100%,0 100%)}
</style>
</head>
<body>

<section class="spread spread--outside" aria-label="Brochure outside">
  <article class="panel flap">
    <div class="photo photo--sunset" role="img" aria-label="Photo of a truck on a highway at sunset"></div>
    <div class="shape shape--swoosh"></div>
    <div class="shape shape--white"></div>
    <div class="copy">
      <h3 class="section-title">Capacity</h3>
      <p class="body-text">Our extensive third-party capacity network gives shippers options at a price you name. From standard loads to time-critical freight, we line up the right carrier for all of your cargo.</p>
      <h3 class="section-title">Expertise</h3>
      <p class="body-text">Through our large network of carriers and backhaul partners we match your freight with the best truck on the lane. Our brokers know each market, each rate and each carrier, so your shipment moves on time and on budget, every time.</p>
    </div>
    <div class="shape shape--footer"></div>
    <p class="quote">Get a Quote</p>
    <p class="web">www.haulvento.example</p>
  </article>

  <article class="panel back">
    <div class="shape shape--top"></div>
    <div class="brand"><span class="brand__square"></span>Haulvento Freight Logistics</div>
    <div class="portrait" role="img" aria-label="Portrait photo of Mark Velinstrom"></div>
    <p class="name">Mark Velinstrom</p>
    <p class="title">Certified Freight Broker</p>
    <ul class="contact">
      <li><svg width="16" height="16" viewBox="0 0 16 16"><path d="M3 1h3l1 4-2 1a9 9 0 0 0 5 5l1-2 4 1v3a2 2 0 0 1-2 2A13 13 0 0 1 1 3a2 2 0 0 1 2-2z" fill="#fff"/></svg>866-417-3961</li>
      <li><svg width="16" height="16" viewBox="0 0 16 16"><rect x="1" y="3" width="14" height="10" rx="1" fill="none" stroke="#fff" stroke-width="1.6"/><path d="M1.5 4l6.5 5 6.5-5" fill="none" stroke="#fff" stroke-width="1.6"/></svg>Mark@haulvento.example</li>
      <li><svg width="16" height="16" viewBox="0 0 16 16"><path d="M8 1a5 5 0 0 1 5 5c0 4-5 9-5 9S3 10 3 6a5 5 0 0 1 5-5z" fill="#fff"/><circle cx="8" cy="6" r="2" fill="#b3151b"/></svg>3175 W. Brindle Avenue, #51872<br>Denver, CO 80391</li>
    </ul>
    <div class="shape shape--bottom"></div>
  </article>

  <article class="panel cover">
    <div class="shape shape--head"></div>
    <div class="brand"><span class="brand__square"></span>Haulvento Freight Logistics</div>
    <div class="photo photo--truck" role="img" aria-label="Photo of a red semi truck speeding along a highway"></div>
    <div class="shape shape--dark"></div>
    <div class="shape shape--band"></div>
    <p class="tagline">Fast Shipping Relief</p>
    <p class="web">www.haulvento.example</p>
  </article>
</section>

<section class="spread spread--inside" aria-label="Brochure inside">
  <article class="panel benefits">
    <div class="shape shape--corner"></div>
    <h2 class="headline">We find reliable trucks <em>QUICKLY</em> and at the <em>BEST RATE.</em></h2>
    <div class="rule"></div>
    <p class="body-text">You tell us the rate you want to pay and we'll negotiate that rate for you.</p>
    <p class="body-text">We are certified freight brokers trained to the highest standard of proficiency.</p>
    <p class="body-text">Top quality management who understand your business processes, goals and requirements.</p>
    <p class="body-text">In the event of a loss or damage claim we negotiate that claim on your behalf AT NO COST TO YOU.</p>
    <p class="body-text">We distinguish ourselves with the expertise to fulfill ALL our customers' information and logistical needs.</p>
    <div class="shape shape--swoosh"></div>
    <div class="shape shape--grey"></div>
  </article>

  <article class="panel network">
    <div class="photo photo--rig" role="img" aria-label="Photo of a blue and red semi truck on the road"></div>
    <div class="copy">
      <p class="lead">With a network of over 7,000 Motor Carriers, we are able to locate backhaulers that match your shipping and transportation needs.</p>
      <div class="rule"></div>
      <p>Expertise to handle all shipment types: LTL, Intermodal, Expedited and Hazardous to handle ALL your transportation needs.</p>
      <p>Ability to add value to multiple parts of your organization.</p>
      <p>Our team of professionals is continually updated on evolving industry trends.</p>
    </div>
    <div class="photo photo--yard" role="img" aria-label="Black and white photo of trucks in a freight yard"></div>
  </article>

  <article class="panel service">
    <div class="photo photo--road" role="img" aria-label="Photo of an open highway under a bright sky"></div>
    <div class="shape shape--wedge"></div>
    <div class="copy">
      <h3 class="section-title">Training</h3>
      <p class="body-text">Each Haulvento broker has achieved the highest level of industry certification possible. Our team trains to protect your goods, your schedule and your company from liability in any cargo claim.</p>
      <h3 class="section-title">Customer Service</h3>
      <p class="body-text">Haulvento understands that the cost of freight can mean the difference between profit and loss. We realize that our success depends on building long-term relationships with our customers, and our commitment is to keep your costs low and your service high from start to finish.</p>
    </div>
    <div class="shape shape--foot"></div>
  </article>
</section>

</body>
</html>
```